JT & WE Shearing Pty Ltd

We already have an existing logo created by Lumen Quarry however we have restructured to a company. We would like someone to add Pty Ltd to our business name please.

Colors

Designer to choose only greyscale colors for use in the design.

```html
<!DOCTYPE html>
<html lang="en">
<head>
<meta charset="utf-8">
<title>JT &amp; WE Shearing Pty Ltd – Business Card</title>
<link rel="stylesheet" href="https://fonts.googleapis.com/css2?family=Merriweather:wght@900&family=Lato:wght@400&display=swap">
<style>
  :root {
    --backdrop: #555555;
    --ink: #111111;
    --paper: #ffffff;
    --card-black: #050505;
    --muted: #2a2a2a;
  }
  * { box-sizing: border-box; margin: 0; padding: 0; }
  html, body {
    width: 1200px;
    height: 1200px;
    overflow: hidden;
    background: var(--backdrop);
  }
  .canvas {
    position: relative;
    width: 1200px;
    height: 1200px;
  }
  .card {
    position: absolute;
    left: 300px;
    width: 600px;
    height: 330px;
    border-radius: 70px 0 70px 0;
    box-shadow: 0 10px 24px rgba(0,0,0,0.35);
  }
  .card--back {
    top: 220px;
    background: var(--card-black);
  }
  .card--front {
    top: 600px;
    background: var(--paper);
  }

  .brand-name {
    position: absolute;
    width: 240px;
    font-family: "Merriweather", Georgia, serif;
    font-weight: 900;
    font-size: 26px;
    line-height: 1.3;
    text-align: center;
  }
  .card--back .brand-name {
    color: var(--paper);
    left: 180px;
    top: 116px;
  }
  .card--front .brand-name {
    color: var(--ink);
    left: 320px;
    top: 64px;
  }

  .holder-name {
    position: absolute;
    left: 50px;
    top: 126px;
    font-family: "Merriweather", Georgia, serif;
    font-weight: 900;
    font-size: 17px;
    letter-spacing: 0.5px;
    color: var(--ink);
  }
  .contact-list {
    position: absolute;
    left: 46px;
    top: 180px;
    list-style: none;
    font-family: "Lato", Arial, sans-serif;
    font-size: 16px;
    color: var(--muted);
  }
  .contact-list li {
    display: flex;
    align-items: center;
    gap: 8px;
    height: 28px;
  }
  .contact-icon { width: 20px; height: 20px; flex: none; }
</style>
</head>
<body>
<main class="canvas">
  <section class="card card--back" aria-label="Card back">
    <p class="brand-name">JT &amp; WE Shearing Pty Ltd</p>
  </section>

  <section class="card card--front" aria-label="Card front">
    <h1 class="holder-name">TOM ELLERBY</h1>
    <ul class="contact-list">
      <li>
        <svg class="contact-icon" viewBox="0 0 20 20" aria-hidden="true">
          <circle cx="10" cy="10" r="10" fill="#111"/>
          <path d="M6.5 5.5c.6-.5 1.3-.4 1.6.2l.8 1.5c.2.5 0 .9-.4 1.2l-.5.4c.5 1.2 1.4 2.1 2.6 2.6l.4-.5c.3-.4.7-.6 1.2-.4l1.5.8c.6.3.7 1 .2 1.6-.8.9-2 1.2-3.2.6-2-1-3.6-2.6-4.6-4.6-.6-1.2-.3-2.4.4-3.4z" fill="#fff"/>
        </svg>
        <span>044 5128394</span>
      </li>
      <li>
        <svg class="contact-icon" viewBox="0 0 20 20" aria-hidden="true">
          <circle cx="10" cy="10" r="10" fill="#111"/>
          <rect x="5" y="6.5" width="10" height="7" fill="none" stroke="#fff" stroke-width="1.3"/>
          <path d="M5 6.5l5 4 5-4" fill="none" stroke="#fff" stroke-width="1.3"/>
        </svg>
        <span>hello@jtweshearing.net</span>
      </li>
      <li>
        <svg class="contact-icon" viewBox="0 0 20 20" aria-hidden="true">
          <circle cx="10" cy="10" r="10" fill="#111"/>
          <path d="M10 4.5a3.6 3.6 0 0 0-3.6 3.6c0 2.7 3.6 7 3.6 7s3.6-4.3 3.6-7A3.6 3.6 0 0 0 10 4.5z" fill="#fff"/>
          <circle cx="10" cy="8.1" r="1.3" fill="#111"/>
        </svg>
        <span>PO Box 418 Brenfield WA 6350</span>
      </li>
    </ul>
    <p class="brand-name">JT &amp; WE Shearing Pty Ltd</p>
  </section>
</main>
</body>
</html>
```